Orvale Foods Signage for store front

I would like a design for store frontage sign. Please see attach design layout and bright colors I like. I like the outline of the blue of each food item. Company name is Orvale Foods. I would like the words " Wholesale Restaurant Supplier" underneath our company's name. I would like "chuyên bán thịt, hải sản, hải sản, gia cầm và các sản phẩm tươi" below "Meat, Seafood, Poultry, Grocery and Fresh Produce". I really lik ethe Maple Harvest colors.

Target Market(s)

restaurant owners

Industry/Entity Type

Store

Font styles to use
Serif

Requirements
Must have
• colorful lettering and design
Should not have
• real picture of food or meat

```html
<!DOCTYPE html>
<html lang="en">
<head>
<meta charset="utf-8">
<title>Orvale Foods Storefront Sign</title>
<link rel="stylesheet" href="https://fonts.googleapis.com/css2?family=Anton&family=Open+Sans:wght@700&family=Roboto:wght@700&display=swap">
<style>
  :root {
    --backdrop: #e9e9ec;
    --sign-white: #ffffff;
    --sign-edge: #f1f1f3;
    --indigo: #2f2a90;
    --indigo-deep: #241f78;
    --leaf-green: #5aa51e;
    --gold-dark: #eea200;
    --gold-mid: #ffc400;
    --gold-light: #fff000;
    --stitch: #ffffff;
  }
  html, body {
    margin: 0;
    padding: 0;
    width: 994px;
    height: 1200px;
    overflow: hidden;
    background: var(--backdrop);
  }
  .canvas {
    position: relative;
    width: 994px;
    height: 1200px;
  }
  .storefront-sign {
    position: absolute;
    left: 27px;
    top: 424px;
    width: 940px;
    height: 353px;
    box-shadow: 0 10px 24px rgba(0,0,0,0.25);
  }
  .brand-name {
    font-family: "Anton", "Oswald", sans-serif;
    font-size: 62px;
    letter-spacing: 0.5px;
  }
  .tagline {
    font-family: "Roboto", Arial, sans-serif;
    font-weight: 700;
    font-size: 16.5px;
    fill: var(--leaf-green);
    letter-spacing: 0.3px;
  }
  .ribbon-text {
    font-family: "Anton", "Oswald", sans-serif;
    font-size: 23px;
    fill: var(--indigo);
    letter-spacing: 0.5px;
  }
  .product-line {
    font-family: "Open Sans", Arial, sans-serif;
    font-weight: 700;
    font-size: 11.5px;
    fill: #ffffff;
  }
</style>
</head>
<body>
<div class="canvas">
  <svg class="storefront-sign" viewBox="0 0 940 353" width="940" height="353" xmlns="http://www.w3.org/2000/svg">
    <defs>
      <linearGradient id="sign-face" x1="0" y1="0" x2="1" y2="1">
        <stop offset="0" stop-color="#ffffff"/>
        <stop offset="1" stop-color="#f1f1f3"/>
      </linearGradient>
      <linearGradient id="ribbon-gold" x1="0" y1="0" x2="1" y2="0">
        <stop offset="0" stop-color="#eea200"/>
        <stop offset="0.5" stop-color="#ffc400"/>
        <stop offset="1" stop-color="#f5b800"/>
      </linearGradient>
      <linearGradient id="brand-fill" x1="0" y1="0" x2="0" y2="1">
        <stop offset="0" stop-color="#4a44b8"/>
        <stop offset="1" stop-color="#241f78"/>
      </linearGradient>
      <radialGradient id="produce-tones" cx="0.5" cy="0.5" r="0.6">
        <stop offset="0" stop-color="#f1e6c8"/>
        <stop offset="0.45" stop-color="#e2512b"/>
        <stop offset="1" stop-color="#3a9a2c"/>
      </radialGradient>
      <radialGradient id="banner-shadow" cx="0.5" cy="0.5" r="0.5">
        <stop offset="0" stop-color="rgba(0,0,0,0.35)"/>
        <stop offset="1" stop-color="rgba(0,0,0,0)"/>
      </radialGradient>
    </defs>

    <rect class="sign-face" x="0" y="0" width="940" height="353" fill="url(#sign-face)"/>

    <text class="brand-name" x="470" y="71" text-anchor="middle" fill="url(#brand-fill)">ORVALE FOODS</text>
    <text class="tagline" x="470" y="94" text-anchor="middle">WHOLESALE RESTAURANT SUPPLIER</text>

    <g class="gold-ribbon">
      <polygon points="158,148 262,148 262,240 158,240 200,194" fill="var(--gold-dark)"/>
      <polygon points="782,148 678,148 678,240 782,240 740,194" fill="var(--gold-light)"/>
      <polygon points="259,227 270,240 262,240" fill="#b57800"/>
      <polygon points="681,227 670,240 678,240" fill="#b57800"/>
      <rect x="259" y="139" width="422" height="88" fill="url(#ribbon-gold)"/>
    </g>

    <rect class="produce-art" role="img" aria-label="Illustration of fresh produce with blue outlines: shrimp, tomato, carrot, pepper, onion and a cut of meat" x="386" y="100" width="180" height="178" rx="60" fill="url(#produce-tones)"/>

    <g class="ribbon-labels">
      <text class="ribbon-text" x="276" y="170">QUALITY &amp;</text>
      <text class="ribbon-text" x="276" y="197">SERVICE</text>
      <text class="ribbon-text" x="576" y="180">SINCE</text>
      <text class="ribbon-text" x="576" y="208">1982</text>
    </g>

    <ellipse cx="470" cy="343" rx="200" ry="6" fill="url(#banner-shadow)"/>
    <g class="product-banner">
      <polygon points="238,292 704,292 692,315 704,338 238,338 250,315" fill="var(--indigo)"/>
      <polygon points="246,296 696,296 686,315 696,334 246,334 256,315" fill="none" stroke="var(--stitch)" stroke-width="1" stroke-dasharray="3 3"/>
      <text class="product-line" x="471" y="311" text-anchor="middle">chuyên bán thịt, hải sản, hải sản, gia cầm và các sản phẩm tươi"</text>
      <text class="product-line" x="471" y="327" text-anchor="middle">Meat, Seafood, Poultry, Grocery and Fresh Produce.</text>
    </g>
  </svg>
</div>
</body>
</html>
```